Business Card for TLK Field Services

Would like a large logo on one side. On the other side, logo on one side and company phone number, address, and email on the other side. I don't have a logo so please create one for us.
Updates
I don't have a logo, so please create one for us.
Target Market(s)
Land Surveying
Industry/Entity Type
Surveyor
Contact Information for Business Card
Would like a large logo on one side. On the other side, logo on one side and company phone number, address, and email on the other side
Requirements
Nice to have
- would like the initials to be incorporated with the logo

```html
<!DOCTYPE html>
<html lang="en">
<head>
<meta charset="utf-8">
<title>TLK Field Services – Business Card</title>
<link rel="stylesheet" href="https://fonts.googleapis.com/css2?family=Cinzel:wght@500&family=Open+Sans:wght@400;600&display=swap">
<style>
  :root {
    --page: #e9e9e9;
    --red: #d42027;
    --black: #0b0b0c;
    --white: #ffffff;
    --ink: #1c1c1c;
  }
  * { box-sizing: border-box; margin: 0; padding: 0; }
  html, body { width: 1200px; height: 903px; overflow: hidden; }
  body {
    background: var(--page);
    font-family: "Open Sans", Arial, sans-serif;
    position: relative;
  }
  .card {
    position: absolute;
    top: 297px;
    width: 540px;
    height: 309px;
    overflow: hidden;
    box-shadow: 0 8px 24px rgba(0,0,0,.18);
  }
  .card svg { position: absolute; inset: 0; width: 100%; height: 100%; }
  .card--front { left: 40px; background: var(--black); }
  .card--back { left: 620px; background: var(--red); }

  .front-mark {
    position: absolute;
    inset: 0;
    display: flex;
    flex-direction: column;
    align-items: center;
    justify-content: center;
    color: var(--white);
    font-weight: 600;
    line-height: 1;
  }
  .front-mark__initials { font-size: 64px; letter-spacing: 2px; }
  .front-mark__words { font-size: 26px; margin-top: 6px; }

  .back-mark {
    position: absolute;
    left: 28px;
    top: 70px;
    color: var(--ink);
    font-weight: 600;
    line-height: 1;
  }
  .back-mark__initials { font-size: 34px; letter-spacing: 1px; }
  .back-mark__words { font-size: 16px; margin-top: 4px; }

  .person { position: absolute; left: 330px; top: 46px; color: var(--white); }
  .person__name { font-family: "Cinzel", Georgia, serif; font-weight: 500; font-size: 22px; letter-spacing: 1px; }
  .person__title { font-size: 11px; margin-top: 2px; }

  .contact {
    position: absolute;
    left: 250px;
    top: 116px;
    list-style: none;
    color: var(--white);
    font-size: 13px;
    line-height: 20px;
  }
  .address {
    position: absolute;
    left: 230px;
    top: 214px;
    color: var(--white);
    font-style: normal;
    font-size: 11px;
    line-height: 16px;
  }
</style>
</head>
<body>

<section class="card card--front" aria-label="Business card front">
  <svg viewBox="0 0 540 309" aria-hidden="true">
    <circle cx="270" cy="154" r="222" fill="var(--white)"/>
    <circle cx="270" cy="154" r="198" fill="var(--black)"/>
    <circle cx="270" cy="154" r="160" fill="var(--red)"/>
  </svg>
  <div class="front-mark">
    <span class="front-mark__initials">TLK</span>
    <span class="front-mark__words">Field Services</span>
  </div>
</section>

<section class="card card--back" aria-label="Business card back">
  <svg viewBox="0 0 540 309" aria-hidden="true">
    <circle cx="20" cy="150" r="200" fill="var(--white)"/>
  </svg>
  <div class="back-mark">
    <div class="back-mark__initials">TLK</div>
    <div class="back-mark__words">Field Services</div>
  </div>
  <div class="person">
    <div class="person__name">Your Name</div>
    <div class="person__title">Job Title</div>
  </div>
  <ul class="contact">
    <li>P: 101 1010</li>
    <li>M: 1234567890</li>
    <li>E: services@tlkmail.co.nz</li>
    <li>www.tlkfieldservices.co.nz</li>
  </ul>
  <address class="address">
    TLK Field Services<br>
    First Floor, 14 Harbour Lane, Westbrook<br>
    PO Box 512 300, Northvale
  </address>
</section>

</body>
</html>
```